AMBER AND STONE WEB

We need a home design in wordpress, we have now a web but we would like to improve it. Our current web is www.amberandstonevillas.example Our business is holliday rental of villas in Ibiza. Our guest must know that we are a reliable company, professional and with experience and good reviews. We want them to click in our reservation engine: https://bookings.amberandstonevillas.example/en/ and make reservation in our website. We would also like to say that all the properties that we have are just us who commercialize so we have best price available. Many people are going to see our villas in staylister.example and look to our website to make a reservation with us so we need to show them that they are at the right place and click at our link to our reservation engine. What make us special is that we are a local company, we are from Ibiza, Our guests are always received in person by the Amber and Stone Villas team. You will enjoy extensive tourist information when you check in and during the entire stay. You will be attended by ChatLoop and calls, always happy to help so that you have a happy and fun stay! Our guest stay is better than in hotel as they have more spece, private swiming pool, private garden, barbeque ... To rent a villa is the best way to stay in Ibiza. We also have a promotional video: https://vidshare.example/Qm7tLp2Xz9A Let our philosophy be shown, we think that coming on holiday to Ibiza implies seeing the nature that we have in Ibiza, hence our name AMBER AND STONE, like the pins that almost touch the sea in Ibiza, or the posidonea meadows where the intense green of the seaweed and the blue of the sea. We are aware of the environment, and we love Ibiza. For us, the client who visits Ibiza, should rent a car, go around the island, eat in a restaurant one day in front of the sea, is a night of partying to the discs, go shopping, visit the ancient heritage of Umanity, make some aquatic sport, enjoy the pool, those are for us Ibiza.

Target Market(s)

Europe, people from Holand, UK, Germany, France, Spain ...

Industry/Entity Type

Tourism

Colors

Designer to choose colors to be used in the design.

Requirements
Must have
• Pictures of Ibiza.
Nice to have
• Our name Amber and Stone Villas is beacuse in Ibiza there is forest that almost touch the watter of the Mediterranean sea, so you can see green of the forest and blue of the sea and the sky. And also beacause under the watter of the sea there is a plant called Posidonia that is also green please see the picture of posidonia.

```html
<!DOCTYPE html>
<html lang="en">
<head>
<meta charset="utf-8">
<title>Amber and Stone Villas – Holiday Villas in Ibiza</title>
<link rel="stylesheet" href="https://fonts.googleapis.com/css2?family=Cormorant+Garamond:wght@500;600;700&family=Open+Sans:wght@400;600;700&display=swap">
<style>
:root{
  --teal:#1f9ed6;
  --blue:#2a8fd0;
  --blue-deep:#1d7fbf;
  --green:#4e7a2c;
  --green-dark:#3f6a22;
  --leaf:#6d9a33;
  --ink:#333a40;
  --muted:#777f86;
  --line:#e3e6e8;
  --white:#ffffff;
  --serif:'Cormorant Garamond', Georgia, serif;
  --sans:'Open Sans', Arial, sans-serif;
}
*{box-sizing:border-box;margin:0;padding:0}
html,body{width:1200px;height:2944px;overflow:hidden}
body{font-family:var(--sans);color:var(--ink);background:var(--white);position:relative}

/* top bar */
.topbar{height:48px;background:linear-gradient(90deg,var(--blue-deep),var(--teal) 50%,var(--green));color:#fff;font-size:12px;display:flex;align-items:center;padding:0 80px;gap:28px}
.topbar .item{display:flex;align-items:center;gap:7px}
.topbar .spacer{flex:1}
.topbar .book{background:#fff;color:var(--blue-deep);padding:6px 14px;font-weight:600;border-radius:2px}

/* header */
.header{height:96px;display:flex;align-items:center;padding:0 80px;justify-content:space-between}
.brand{display:flex;align-items:center;gap:12px}
.brand .dot{width:30px;height:30px;border-radius:50%;background:var(--green)}
.brand .name{font-family:var(--serif);font-weight:700;font-size:25px;color:var(--green);letter-spacing:.5px}
.nav{display:flex;gap:34px;font-size:13px}
.nav a{color:var(--ink);text-decoration:none}
.nav a.active{color:var(--teal);border-bottom:2px solid var(--teal);padding-bottom:4px}

/* search */
.search{height:64px;background:var(--teal);display:flex;align-items:flex-end;gap:16px;padding:0 80px 12px}
.field{display:flex;flex-direction:column;gap:4px;color:#fff;font-size:11px}
.field .box{background:#fff;height:26px;border-radius:2px;color:var(--muted);font-size:11px;display:flex;align-items:center;padding:0 10px}
.search .go{background:var(--blue-deep);color:#fff;font-weight:700;font-size:12px;height:26px;width:150px;display:flex;align-items:center;justify-content:center;border-radius:2px;margin-left:auto}

/* hero */
.hero{position:relative;height:580px;background:linear-gradient(180deg,#5b9fd6 0%,#3d7fae 30%,#2e8a86 55%,#4d7b3d 75%,#c6b489 100%);overflow:hidden}
.hero h1{position:absolute;top:170px;left:0;right:0;text-align:center;font-family:var(--serif);font-weight:600;font-size:64px;line-height:66px;color:#fff}
.hero .cta{position:absolute;top:354px;left:530px;width:140px;height:36px;background:#fff;color:var(--ink);font-size:11px;font-weight:700;display:flex;align-items:center;justify-content:center;letter-spacing:.5px}
.arrow{position:absolute;width:34px;height:34px;border-radius:50%;background:rgba(255,255,255,.9);display:flex;align-items:center;justify-content:center}
.hero .wave{position:absolute;left:0;bottom:0;width:1200px;height:90px}

/* welcome */
.welcome{height:440px;position:relative;padding:40px 110px 0;display:flex;gap:60px}
.welcome .text{width:520px;padding-top:4px}
.welcome h2{display:flex;align-items:center;gap:12px;font-family:var(--serif);font-weight:600;font-size:28px;color:var(--green);letter-spacing:1px}
.welcome h3{font-family:var(--serif);font-size:22px;color:var(--ink);margin:14px 0 14px 54px;font-weight:600}
.welcome p{font-size:13px;line-height:21px;color:var(--muted);margin-left:54px}
.btn-green{display:inline-flex;align-items:center;justify-content:center;background:var(--green);color:#fff;font-size:12px;font-weight:600;width:120px;height:36px;margin:24px 0 0 54px}
.welcome .media{width:440px;height:265px;background:linear-gradient(135deg,#6a8d55,#c9b79c 55%,#8aa6b8);position:relative}
.play{position:absolute;left:200px;top:112px;width:42px;height:42px;border-radius:50%;background:rgba(255,255,255,.85)}
.play::after{content:"";position:absolute;left:17px;top:13px;border-left:12px solid var(--green);border-top:8px solid transparent;border-bottom:8px solid transparent}

/* properties */
.properties{height:710px;background:linear-gradient(180deg,var(--blue-deep),var(--teal));position:relative;color:#fff;text-align:center;padding-top:48px}
.section-title{font-family:var(--serif);font-weight:600;font-size:40px}
.properties .lead{font-size:12px;line-height:20px;width:640px;margin:14px auto 0;opacity:.9}
.cards{display:flex;gap:24px;justify-content:center;margin-top:36px}
.card{width:300px;background:#fff;text-align:left;color:var(--ink)}
.card .photo{height:210px}
.card .body{padding:14px 16px 10px}
.card h4{font-family:var(--serif);font-size:20px;font-weight:600;color:var(--green-dark)}
.card .loc{font-size:11px;color:var(--muted);margin-top:3px}
.card .price{background:var(--green);color:#fff;font-size:12px;height:34px;display:flex;align-items:center;justify-content:space-between;padding:0 16px}
.dots{display:flex;gap:8px;justify-content:center;margin-top:22px}
.dots span{width:8px;height:8px;border-radius:50%;background:rgba(255,255,255,.5)}
.dots span.on{background:#fff}
.btn-white{display:inline-flex;width:120px;height:36px;align-items:center;justify-content:center;background:#fff;color:var(--ink);font-size:12px;font-weight:600;margin-top:30px}

/* testimonials */
.testimonials{height:420px;position:relative;padding-top:40px;text-align:center}
.testimonials .section-title{color:var(--blue-deep);display:flex;justify-content:center;align-items:center;gap:14px}
.quote-card{width:640px;height:260px;margin:26px auto 0;background:#fff;box-shadow:0 4px 22px rgba(0,0,0,.12);position:relative;padding:36px 90px 0}
.quote-card .q{position:absolute;font-family:var(--serif);font-size:64px;color:var(--green);line-height:1}
.quote-card p{font-size:13px;line-height:20px;color:var(--muted)}
.avatar{width:60px;height:60px;border-radius:50%;background:linear-gradient(135deg,#c9b3a3,#8b7a6e);margin:18px auto 6px}
.quote-card .who{font-size:12px;color:var(--ink)}
.quote-card .who em{color:var(--muted)}
.tdots{display:flex;gap:8px;justify-content:center;margin-top:16px}
.tdots span{width:8px;height:8px;border-radius:50%;background:#c4cacd}
.tdots span.on{background:var(--muted)}

/* footer */
.footer{height:524px;background:linear-gradient(100deg,var(--blue-deep),var(--teal) 45%,var(--green));color:#fff;padding:58px 120px 0;position:relative}
.cols{display:flex;gap:90px}
.col h5{font-family:var(--serif);font-size:20px;font-weight:600;margin-bottom:18px}
.col ul{list-style:none;font-size:12px;line-height:26px}
.contact li{display:flex;gap:10px;align-items:flex-start}
.news{display:flex;margin-bottom:16px}
.news .in{width:240px;height:32px;background:#fff;color:var(--muted);font-size:11px;display:flex;align-items:center;padding:0 10px}
.news .sub{height:32px;padding:0 16px;background:var(--blue-deep);font-size:12px;display:flex;align-items:center}
.social{display:flex;gap:12px}
.social span{width:18px;height:18px;border:1.5px solid #fff;border-radius:3px}
.copy{position:absolute;left:0;right:0;bottom:28px;text-align:center;font-size:11px;border-top:1px solid rgba(255,255,255,.3);padding-top:20px;margin:0 120px}
</style>
</head>
<body>

<div class="topbar">
  <div class="item"><svg width="12" height="12" viewBox="0 0 24 24" fill="#fff"><path d="M6.6 10.8a15 15 0 006.6 6.6l2.2-2.2c.3-.3.7-.4 1-.2 1.1.4 2.3.6 3.6.6.6 0 1 .4 1 1V20c0 .6-.4 1-1 1C10.6 21 3 13.4 3 4c0-.6.4-1 1-1h3.5c.6 0 1 .4 1 1 0 1.3.2 2.5.6 3.6.1.3 0 .7-.2 1z"/></svg>+34 600 000 123</div>
  <div class="item"><svg width="13" height="10" viewBox="0 0 26 20" fill="none" stroke="#fff" stroke-width="2"><rect x="1" y="1" width="24" height="18"/><path d="M1 1l12 10L25 1"/></svg>hello@amberandstonevillas.example</div>
  <div class="spacer"></div>
  <div class="item">Languages: EN · NL · DE</div>
  <div class="book">Book Now</div>
</div>

<header class="header">
  <div class="brand"><span class="dot"></span><span class="name">AMBER AND STONE</span></div>
  <nav class="nav"><a class="active">Home</a><a>Apartments</a><a>About us</a><a>Contact us</a></nav>
</header>

<form class="search">
  <div class="field">Check in and check out date<div class="box" style="width:210px">Select dates for your stay</div></div>
  <div class="field">Adults<div class="box" style="width:110px">2</div></div>
  <div class="field">No. of guests and rooms<div class="box" style="width:200px">2 guests, 1 room</div></div>
  <div class="field">Promo code<div class="box" style="width:120px">Enter code</div></div>
  <div class="go">SEARCH</div>
</form>

<section class="hero" role="img" aria-label="Turquoise cove in Ibiza with pine-covered cliffs and a sandy beach">
  <h1>The best way to<br>Stay in Ibiza</h1>
  <div class="cta">VIEW PACKAGES</div>
  <div class="arrow" style="left:24px;top:270px"><svg width="12" height="12" viewBox="0 0 12 12"><path d="M8 1L3 6l5 5" stroke="#333" stroke-width="2" fill="none"/></svg></div>
  <div class="arrow" style="right:24px;top:270px"><svg width="12" height="12" viewBox="0 0 12 12"><path d="M4 1l5 5-5 5" stroke="#333" stroke-width="2" fill="none"/></svg></div>
  <svg class="wave" viewBox="0 0 1200 90" preserveAspectRatio="none"><path d="M0 60 C150 20 260 80 420 50 S720 10 860 45 S1080 70 1200 30 L1200 90 L0 90Z" fill="#fff"/></svg>
</section>

<section class="welcome">
  <div class="text">
    <h2><span class="brand"><span class="dot" style="width:40px;height:40px"></span></span>WELCOME TO AMBER AND STONE</h2>
    <h3>Luxury Resort &amp; Rooms</h3>
    <p>Amber and Stone Villas is a local Ibiza company offering private villas with pool, garden and barbecue. Every guest is welcomed in person by our team, who share local tips at check in and stay close by chat and phone for the whole holiday, so your time on the island is easy and fun.</p>
    <a class="btn-green">Learn More</a>
  </div>
  <div class="media" role="img" aria-label="Promotional video still of a white Ibiza villa among palm trees"><span class="play"></span></div>
</section>

<section class="properties">
  <div class="section-title">Properties</div>
  <p class="lead">Every villa we list is offered only by us, so you always get the best available price. Private pool, garden and space to relax, close to beaches, restaurants and the best of the island.</p>
  <div class="arrow" style="left:22px;top:390px"><svg width="12" height="12" viewBox="0 0 12 12"><path d="M8 1L3 6l5 5" stroke="#333" stroke-width="2" fill="none"/></svg></div>
  <div class="arrow" style="right:22px;top:390px"><svg width="12" height="12" viewBox="0 0 12 12"><path d="M4 1l5 5-5 5" stroke="#333" stroke-width="2" fill="none"/></svg></div>
  <div class="cards">
    <article class="card"><div class="photo" role="img" aria-label="Villa living room with wooden beams" style="background:linear-gradient(135deg,#b88d6a,#e4d3bd)"></div><div class="body"><h4>Finca Sa Roca</h4><div class="loc">Sant Josep, Ibiza</div></div><div class="price"><span>▣</span><span>From : €150 per night</span></div></article>
    <article class="card"><div class="photo" role="img" aria-label="Private pool of a villa surrounded by greenery" style="background:linear-gradient(180deg,#7fa9c9,#2d9ad1 60%,#6f8f55)"></div><div class="body"><h4>Finca Sa Roca</h4><div class="loc">Santa Eulària, Ibiza</div></div><div class="price"><span>▣</span><span>From : €150 per night</span></div></article>
    <article class="card"><div class="photo" role="img" aria-label="Villa terrace with outdoor furniture" style="background:linear-gradient(135deg,#8fa6b6,#d9d2c4 60%,#9a8c70)"></div><div class="body"><h4>Finca Sa Roca</h4><div class="loc">Sant Antoni, Ibiza</div></div><div class="price"><span>▣</span><span>From : €150 per night</span></div></article>
  </div>
  <div class="dots"><span class="on"></span><span></span><span></span></div>
  <a class="btn-white">View All</a>
</section>

<section class="testimonials">
  <div class="section-title">Testimonials <span class="dot" style="width:40px;height:40px;border-radius:50%;background:var(--green);display:inline-block"></span></div>
  <div class="quote-card">
    <span class="q" style="left:40px;top:24px">“</span>
    <span class="q" style="right:40px;top:120px">”</span>
    <p>Lovely villa with a private pool and a warm welcome from the team. They gave us great local tips and answered every message quickly. We felt at home from day one and will book again.</p>
    <div class="avatar" role="img" aria-label="Guest portrait"></div>
    <div class="who">Marleen – <em>Guest from Utrecht</em></div>
  </div>
  <div class="tdots"><span class="on"></span><span></span><span></span></div>
</section>

<footer class="footer">
  <div class="cols">
    <div class="col" style="width:150px"><h5>Quick Link</h5><ul><li>Apartments</li><li>About Us</li><li>Contact Us</li></ul></div>
    <div class="col contact" style="width:330px"><h5>Contact Us</h5><ul>
      <li><svg width="12" height="12" viewBox="0 0 24 24" fill="#fff" style="margin-top:7px"><path d="M6.6 10.8a15 15 0 006.6 6.6l2.2-2.2c.3-.3.7-.4 1-.2 1.1.4 2.3.6 3.6.6.6 0 1 .4 1 1V20c0 .6-.4 1-1 1C10.6 21 3 13.4 3 4c0-.6.4-1 1-1h3.5c.6 0 1 .4 1 1 0 1.3.2 2.5.6 3.6.1.3 0 .7-.2 1z"/></svg><span>+34 600 000 123<br>Mon – Sat 9:00 – 19:00</span></li>
      <li><svg width="13" height="10" viewBox="0 0 26 20" fill="none" stroke="#fff" stroke-width="2" style="margin-top:8px"><rect x="1" y="1" width="24" height="18"/><path d="M1 1l12 10L25 1"/></svg><span>hello@amberandstonevillas.example</span></li>
      <li><svg width="12" height="14" viewBox="0 0 24 28" fill="#fff" style="margin-top:6px"><path d="M12 0C5.4 0 0 5.2 0 11.6 0 20 12 28 12 28s12-8 12-16.4C24 5.2 18.6 0 12 0zm0 16a4.5 4.5 0 110-9 4.5 4.5 0 010 9z"/></svg><span>Carrer de la Pineda 12<br>07800 Ibiza, Spain<br>Licence ETV-0000-E</span></li>
    </ul></div>
    <div class="col"><h5>Join Us</h5>
      <div class="news"><div class="in">Enter Your Email</div><div class="sub">Subscribe</div></div>
      <div class="social"><span></span><span></span><span></span><span></span></div>
    </div>
  </div>
  <div class="copy">© 2019 Amber and Stone Villas. All Rights Reserved.</div>
</footer>

</body>
</html>
```